Redesign for Real Estate Lead Generation Site

We are looking for a slight redesign for our real estate lead generation sites.

Here's one of our current sites: www.lbrhousetrends.net

The design should be simple as it is currently, remain only on one page, and nothing too detailed to where it may take a while to load/reload. We also have parallel sites, www.gkmhousetrends.net, www.gkmquickdeals.net, and a few others which all will end up utilizing the same template.

We've found that the majority of the site traffic will come from print advertising, not as much SEO. But also understand the more simple the site, the greater likelihood a user may find us through search engines. Another reason we want to keep it rather simple and clean.

The content on the page needs to remain the same, but with additional spaces for one written paragraph testimonial, and an area where we can incorporate a video. Originally, the ideal spot would be the open white space below the social media logos, but we are open to different ideas as you create the redesign.

A change in colors and simple graphics is what we're looking for most along with the testimonial / video additions. Also, we have a new logo we need incorporated into the site somewhere: http://www.bertoprintworks.net/MV-Crew-Estates.zip to download the file in different formates.

Here is our main site, www.mvcrewestates.net through wordpress, so you can get an idea of what folks go to once they've signed up and received a confirm e-mail.

Please contact us if you have any questions. Good luck and thanks for submitting!

```html
<!DOCTYPE html>
<html lang="en">
<head>
<meta charset="utf-8">
<title>MV Crew Estates – Home Value Report</title>
<link href="https://fonts.googleapis.com/css2?family=Questrial&family=Arimo:wght@400;700&display=swap" rel="stylesheet">
<style>
:root{
  --frame:#231f20;
  --page:#ffffff;
  --ink:#1a1a1a;
  --accent:#f6b21a;
  --accent-dark:#d9930a;
  --nav:#1c1c1c;
  --panel:#dcdcdc;
  --card:#efefef;
  --sky-top:#0f63c4;
  --sky-bottom:#6ec6f5;
  --grass:#5c9a34;
  --red:#c8232b;
}
*{box-sizing:border-box;margin:0;padding:0}
html,body{width:912px;height:1200px;overflow:hidden}
body{background:var(--frame);font-family:"Arimo",Arial,sans-serif;color:var(--ink);position:relative}
.page{position:absolute;left:23px;top:25px;width:870px;height:1142px;background:var(--page)}
.abs{position:absolute}

/* header */
.brand{left:18px;top:14px;display:flex;align-items:center;gap:10px}
.brand-mark{width:26px;height:26px;background:var(--accent)}
.brand-name{font-family:"Questrial",sans-serif;font-size:34px;line-height:1;color:var(--ink);width:170px}
.follow{left:654px;top:35px;font-size:11.5px;color:var(--ink)}
.social{top:14px;width:35px;height:35px;border-radius:5px}
.social.s1{left:735px;background:#e6457d}
.social.s2{left:777px;background:#5cc6f0}
.social.s3{left:823px;background:#e9e9e9;border:1px solid #c9c9c9}
.nav{left:288px;top:86px;width:580px;height:37px;background:linear-gradient(#3a3a3a,var(--nav));border-radius:4px 4px 0 0;font-family:"Questrial",sans-serif;font-size:15px;color:#fff}
.nav a{color:#fff;text-decoration:none;position:absolute;top:9px;white-space:nowrap}
.nav .home{left:14px;top:7px;width:63px;height:23px;border-radius:4px;background:linear-gradient(#ffd25a,var(--accent-dark));color:#1a1a1a;text-align:center;line-height:23px}
.rule{left:0;top:124px;width:870px;height:3px;background:#d9d9d9}
.hero{left:2px;top:127px;width:866px;height:303px;background:linear-gradient(180deg,#1d4f86 0%,#3f6f9a 35%,#9a7a52 58%,#5d7a38 80%,#3f6a26 100%)}

/* form panel */
.form-panel{left:2px;top:444px;width:374px;height:577px;background:var(--panel);border:1px solid #c8c8c8}
.form-intro{left:1px;top:1px;width:370px;height:93px;background:linear-gradient(#5a5a5a,#000);color:#fff;font-family:"Questrial",sans-serif;font-size:13px;line-height:15.6px;padding:5px 8px;border:1px solid #999;white-space:nowrap}
.chev{left:346px;top:100px}
.field{background:#fff;border:1px solid #9a9a9a;border-radius:7px;height:21px;font-size:11px;color:#333;padding:3px 8px;white-space:nowrap}
.label{font-size:11px;color:var(--ink);white-space:nowrap}
.section{font-family:"Questrial",sans-serif;font-size:13.5px;color:var(--ink);white-space:nowrap}
.select{background:#fff;border:1px solid #555;height:14px;font-size:10px;line-height:12px;padding-left:4px}
.select::after{content:"▾";position:absolute;right:2px;top:0;font-size:11px}
.signup{left:96px;top:531px;width:117px;height:36px;border-radius:6px;background:linear-gradient(#6a6a6a,#111);color:#fff;font-family:"Questrial",sans-serif;font-size:22px;text-align:center;line-height:36px;border:1px solid #888}

/* right column */
.card{background:linear-gradient(#fff,var(--card));border:1px solid #cfcfcf;border-radius:6px}
.question{left:395px;top:445px;width:461px;height:86px;font-family:"Questrial",sans-serif;font-size:21.5px;text-align:center;line-height:26px;padding-top:16px;white-space:nowrap}
.testimonial{left:395px;top:543px;width:461px;height:160px;padding:7px 8px}
.testimonial h2{font-family:"Questrial",sans-serif;font-weight:400;font-size:21px;margin-bottom:5px}
.testimonial p{font-size:10.4px;line-height:15.6px;padding:0 3px;white-space:nowrap}
.testimonial .author{margin-top:8px;font-size:11px}
.video{left:395px;top:718px;width:460px;height:288px;background:#000;border:1.5px solid var(--accent);border-radius:6px}
.play{left:186px;top:79px}
.video-cta{left:0;top:180px;width:100%;text-align:center;color:#fff;font-weight:700;font-size:16.5px}

/* footer */
.footer{left:12px;top:1030px;width:847px;height:101px;background:linear-gradient(var(--sky-top),var(--sky-bottom) 80%,var(--grass) 84%,#4a8a2a)}
.footer-house{left:6px;top:10px;width:132px;height:82px;background:linear-gradient(#e8e8e8,#8e6a5a);border-radius:2px}
.footer-text{left:0;top:37px;width:847px;text-align:center;color:#fff;font-size:11.5px;line-height:15.5px;padding-left:6px}
</style>
</head>
<body>
<div class="page">
  <header>
    <div class="abs brand"><span class="brand-mark"></span><span class="brand-name">MV Crew Estates</span></div>
    <div class="abs follow">Follow us on :</div>
    <span class="abs social s1" aria-label="Social profile"></span>
    <span class="abs social s2" aria-label="Social profile"></span>
    <span class="abs social s3" aria-label="Video channel"></span>
    <nav class="abs nav">
      <a class="home">Home</a>
      <a style="left:107px">About Us</a>
      <a style="left:199px">Buyer</a>
      <a style="left:267px">Seller</a>
      <a style="left:334px">Search Listings</a>
      <a style="left:469px">Contact Us</a>
    </nav>
  </header>
  <div class="abs rule"></div>
  <div class="abs hero" role="img" aria-label="Large stone luxury home at dusk with lit windows, lawn and garden"></div>

  <section class="abs form-panel">
    <div class="abs form-intro">Fill out the form below for a FREE Comparative Market<br>Analysis Report from MV Crew Estates for an estimate of<br>your home's current value. The more complete the form<br>the easier it will be to provide an accurate<br>report regarding the value of your home.</div>
    <svg class="abs chev" width="15" height="22" viewBox="0 0 15 22"><path d="M1 2l6.5 6 6.5-6M1 11l6.5 6 6.5-6" fill="none" stroke="#333" stroke-width="3"/></svg>
    <div class="abs field" style="left:14px;top:111px;width:153px">Name...</div>
    <div class="abs field" style="left:14px;top:143px;width:249px">Email...</div>
    <div class="abs field" style="left:14px;top:174px;width:153px">Phone...</div>
    <div class="abs section" style="left:18px;top:210px">Property Address</div>
    <div class="abs label" style="left:18px;top:236px">Street Address</div>
    <div class="abs field" style="left:14px;top:249px;width:302px"></div>
    <div class="abs label" style="left:18px;top:285px">City</div>
    <div class="abs label" style="left:184px;top:285px">State</div>
    <div class="abs label" style="left:232px;top:285px">Zip</div>
    <div class="abs field" style="left:14px;top:300px;width:153px"></div>
    <div class="abs field" style="left:178px;top:300px;width:40px;padding:3px 6px">VA ▾</div>
    <div class="abs field" style="left:224px;top:300px;width:93px"></div>
    <div class="abs section" style="left:19px;top:334px">Property Description</div>
    <div class="abs label" style="left:18px;top:370px">No. Of Bedrooms</div>
    <div class="abs select" style="left:123px;top:372px;width:26px">3</div>
    <div class="abs label" style="left:166px;top:370px">No. Of Bathrooms</div>
    <div class="abs select" style="left:280px;top:372px;width:26px">2</div>
    <div class="abs label" style="left:18px;top:401px">Conditions</div>
    <div class="abs select" style="left:89px;top:403px;width:62px"></div>
    <div class="abs label" style="left:18px;top:431px">Additional comments</div>
    <div class="abs field" style="left:14px;top:449px;width:301px;height:75px"></div>
    <div class="abs signup">Sign Up!</div>
  </section>

  <div class="abs card question">"What is the current market value of my<br>home in today's market?"</div>

  <section class="abs card testimonial">
    <h2>Testimonial</h2>
    <p>Lorem Ipsum is simply dummy text of the printing and typesetting industry. Lorem Ipsum<br>has been the industry's standard dummy text ever since the 1500s, when an unknown<br>printer took a galley of type and scrambled it to make a type specimen book. It has sur-<br>vived not only five centuries, but also the leap into electronic typesetting, remaining es-<br>sentially unchanged.</p>
    <p class="author">Dale Morrow (Riverside)</p>
  </section>

  <section class="abs video">
    <svg class="abs play" width="86" height="86" viewBox="0 0 86 86">
      <circle cx="43" cy="43" r="41" fill="#ddd"/>
      <circle cx="43" cy="43" r="36" fill="var(--red)"/>
      <path d="M33 26v34l28-17z" fill="#fff"/>
    </svg>
    <div class="abs video-cta">Click to play the video</div>
  </section>

  <footer class="abs footer">
    <div class="abs footer-house" role="img" aria-label="Two-storey suburban house with garage"></div>
    <div class="abs footer-text">MV Crew Estates :: Harbor 45 Summit Group :: 877-555-0142 :: info@mvcrewestates.net<br>© 2010 MV Crew Estates</div>
  </footer>
</div>
</body>
</html>
```